Leadership Development Booklet

Design a booklet to be used in a training course on leadership development. The training material is provided in the word doc, but need to enhance the look.

Target Market(s)

Executive Managers

Industry/Entity Type

Water Industry

Font styles to use
Other font styles liked:
• Helvetica

Colors
0054AA
0677BA
7BADD7
CADEEF
E8F1F8

```html
<!DOCTYPE html>
<html lang="en">
<head>
<meta charset="utf-8">
<title>Norva Leadership Profile Design 2023 – Booklet</title>
<link rel="stylesheet" href="https://fonts.googleapis.com/css2?family=Archivo+Black&family=Arimo:ital,wght@0,400;0,700;1,400;1,700&display=swap">
<style>
  :root{
    --stage:#e3e3e5;
    --paper:#f3f3f4;
    --brand:#3b3aa6;
    --brand-dark:#2e3b8e;
    --steel:#4b62a3;
    --ink:#58585a;
    --ink-soft:#8a8a8d;
    --rule:#d2d2d6;
    --row:#e7e7ea;
    --num:#d8d8dc;
  }
  *{box-sizing:border-box;margin:0;padding:0}
  html,body{width:1200px;height:2400px;overflow:hidden;background:var(--stage)}
  body{position:relative;font-family:"Arimo",Helvetica,Arial,sans-serif;color:var(--ink)}
  .page{position:absolute;width:520px;height:735px;background:var(--paper);overflow:hidden;box-shadow:0 6px 18px rgba(0,0,0,.12)}
  .spread{position:absolute;width:1040px;height:735px;background:var(--paper);overflow:hidden;box-shadow:0 6px 18px rgba(0,0,0,.12)}
  .art{position:absolute;inset:0;width:100%;height:100%}
  .front-cover{left:340px;top:40px}
  .inner-spread{left:80px;top:825px}
  .outer-spread{left:80px;top:1620px}
  .outer-spread .front-cover{left:520px;top:0;box-shadow:none}

  /* cover title block */
  .cover-title{position:absolute;left:50px;top:478px;width:400px}
  .wordmark{font-family:"Arimo",sans-serif;font-weight:700;font-size:38px;color:var(--brand);letter-spacing:2px;padding-left:150px;line-height:1}
  .cover-heading{font-family:"Archivo Black",sans-serif;font-size:54px;color:var(--ink);line-height:1;margin-top:8px;letter-spacing:-1px}
  .cover-sub{font-family:"Arimo",sans-serif;font-size:27px;color:var(--brand);letter-spacing:1px;margin-top:6px}
  .cover-rule{width:60px;height:2px;background:var(--ink-soft);margin:16px 0 0 110px}

  /* module page */
  .module-label{position:absolute;left:48px;top:40px;font-size:19px}
  .module-title{position:absolute;left:46px;top:62px;font-family:"Archivo Black",sans-serif;font-size:27px;color:var(--brand)}
  .quote-box{position:absolute;left:40px;top:120px;width:440px;height:118px;border:1.5px solid var(--ink-soft);border-radius:26px;padding:22px 30px 0 40px;font-size:13px;line-height:1.4}
  .quote-box .mark{position:absolute;font-family:"Archivo Black",sans-serif;font-size:44px;color:var(--brand);line-height:1;background:var(--paper);padding:0 4px}
  .quote-box .open{left:10px;top:-18px}
  .quote-box .close{right:26px;bottom:-26px}
  .quote-box cite{display:block;font-style:normal;font-weight:700;font-size:12px;color:var(--brand);margin-top:4px;padding-left:30px}
  .objectives-banner{position:absolute;left:0;top:262px;width:300px;height:34px;background:var(--brand);clip-path:polygon(0 0,100% 0,92% 100%,0 100%);color:#fff;font-weight:700;font-style:italic;font-size:17px;padding:7px 0 0 40px}
  .objectives-list{position:absolute;left:40px;top:310px;list-style:none;font-size:14px;line-height:21px}
  .objectives-list li{display:flex;align-items:center;gap:10px}
  .tick{width:13px;height:13px;flex:none}

  /* exercise page */
  .exercise{position:absolute;left:560px;top:40px;width:450px}
  .exercise-title{font-family:"Archivo Black",sans-serif;font-size:26px;color:var(--ink)}
  .exercise-title span{color:var(--brand)}
  .exercise-note{font-size:11px;margin-top:4px}
  .expectations{position:absolute;left:550px;top:100px;width:460px;border:1px solid var(--rule);border-collapse:collapse}
  .expectations th{height:30px;background:var(--brand);color:#fff;font-size:11px;font-weight:700;text-align:right;padding:0 12px;letter-spacing:.3px}
  .expectations th.blank{background:transparent;width:50px}
  .expectations td{height:36px;border-bottom:3px solid var(--paper);background:var(--row)}
  .expectations td.num{background:var(--num);font-weight:700;font-size:15px;color:var(--ink);text-align:center}
  .expectations tr.spare td{background:transparent;height:50px;border:none}

  /* back cover */
  .back-ghost{position:absolute;left:40px;top:270px;font-family:"Arimo",sans-serif;font-weight:700;font-size:120px;color:#e2e2e5;letter-spacing:4px;line-height:1}
  .back-wordmark{position:absolute;left:70px;top:470px;font-weight:700;font-size:38px;color:var(--brand);letter-spacing:2px;line-height:1}
  .back-address{position:absolute;left:260px;top:470px;font-size:14px;line-height:18px;font-style:normal;color:var(--ink)}
</style>
</head>
<body>

<svg width="0" height="0" style="position:absolute" aria-hidden="true">
  <defs>
    <linearGradient id="office-tone" x1="0" y1="0" x2="1" y2="1">
      <stop offset="0" stop-color="#f4f6f9"/>
      <stop offset=".55" stop-color="#c9cfd8"/>
      <stop offset="1" stop-color="#6d7584"/>
    </linearGradient>
    <linearGradient id="sunset-tone" x1="0" y1="0" x2="1" y2="1">
      <stop offset="0" stop-color="#2a2c38"/>
      <stop offset=".45" stop-color="#e8a04a"/>
      <stop offset=".7" stop-color="#b88a6e"/>
      <stop offset="1" stop-color="#3a3f4c"/>
    </linearGradient>
    <symbol id="cover-art" viewBox="0 0 520 735">
      <g role="img" aria-label="Photo: a presenter speaking to seated colleagues in a bright office">
        <polygon points="120,0 520,0 520,395 250,335" fill="url(#office-tone)"/>
      </g>
      <polygon points="0,0 120,0 250,335 205,350 0,150" fill="var(--brand)"/>
      <polygon points="205,335 520,405 520,440 215,365" fill="var(--steel)"/>
      <polygon points="205,335 520,405 520,415 210,345" fill="var(--brand-dark)"/>
      <polygon points="410,440 520,440 520,530" fill="var(--brand)"/>
    </symbol>
  </defs>
</svg>

<!-- Front cover -->
<section class="page front-cover" aria-label="Front cover">
  <svg class="art" viewBox="0 0 520 735"><use href="#cover-art"/></svg>
  <div class="cover-title">
    <div class="wordmark">NORVA</div>
    <h1 class="cover-heading">LEADERSHIP</h1>
    <p class="cover-sub">PROFILE DESIGN 2023</p>
    <div class="cover-rule"></div>
  </div>
</section>

<!-- Inner spread -->
<section class="spread inner-spread" aria-label="Module 1 spread">
  <svg class="art" viewBox="0 0 1040 735">
    <path d="M0,460 Q230,420 470,470 L470,505 L0,530 Z" fill="#7b7b7e"/>
    <g role="img" aria-label="Photo: silhouetted business team at sunset blended with a thoughtful businessman and city skyline">
      <polygon points="0,555 560,585 600,420 800,400 830,480 930,735 0,735" fill="url(#sunset-tone)"/>
    </g>
    <polygon points="0,525 660,568 640,592 0,555" fill="var(--brand)"/>
    <polygon points="830,480 1040,520 930,735" fill="var(--brand)"/>
    <g role="img" aria-label="Illustration: small crowd of figures">
      <rect x="330" y="355" width="160" height="50" rx="6" fill="#dfe0e6"/>
    </g>
    <line x1="520" y1="0" x2="520" y2="735" stroke="#dcdce0" stroke-width="2"/>
  </svg>

  <p class="module-label">Module 1:</p>
  <h2 class="module-title">Leadership Responsibilities</h2>
  <blockquote class="quote-box">
    <span class="mark open">“</span>
    Before you are a leader, success is all about growing yourself. When you become a leader, success is all about growing others.
    <cite>– Martin Hale (CEO of Corvane Industries from 1981-2001)</cite>
    <span class="mark close">”</span>
  </blockquote>
  <div class="objectives-banner">Leaning Objectives:</div>
  <ul class="objectives-list">
    <li><svg class="tick" viewBox="0 0 13 13"><rect x=".75" y=".75" width="11.5" height="11.5" fill="none" stroke="var(--brand)" stroke-width="1.5"/><path d="M3 6.5l2.5 2.5L10 3.5" fill="none" stroke="var(--brand)" stroke-width="1.6"/></svg>Norva Mission, Vision &amp; Values</li>
    <li><svg class="tick" viewBox="0 0 13 13"><rect x=".75" y=".75" width="11.5" height="11.5" fill="none" stroke="var(--brand)" stroke-width="1.5"/><path d="M3 6.5l2.5 2.5L10 3.5" fill="none" stroke="var(--brand)" stroke-width="1.6"/></svg>Eight Customer Promises</li>
    <li><svg class="tick" viewBox="0 0 13 13"><rect x=".75" y=".75" width="11.5" height="11.5" fill="none" stroke="var(--brand)" stroke-width="1.5"/><path d="M3 6.5l2.5 2.5L10 3.5" fill="none" stroke="var(--brand)" stroke-width="1.6"/></svg>Understanding our Strategic Goals</li>
    <li><svg class="tick" viewBox="0 0 13 13"><rect x=".75" y=".75" width="11.5" height="11.5" fill="none" stroke="var(--brand)" stroke-width="1.5"/><path d="M3 6.5l2.5 2.5L10 3.5" fill="none" stroke="var(--brand)" stroke-width="1.6"/></svg>Creating &amp; Communicating Your Vision</li>
    <li><svg class="tick" viewBox="0 0 13 13"><rect x=".75" y=".75" width="11.5" height="11.5" fill="none" stroke="var(--brand)" stroke-width="1.5"/><path d="M3 6.5l2.5 2.5L10 3.5" fill="none" stroke="var(--brand)" stroke-width="1.6"/></svg>Introduction to Managerial Leadership</li>
    <li><svg class="tick" viewBox="0 0 13 13"><rect x=".75" y=".75" width="11.5" height="11.5" fill="none" stroke="var(--brand)" stroke-width="1.5"/><path d="M3 6.5l2.5 2.5L10 3.5" fill="none" stroke="var(--brand)" stroke-width="1.6"/></svg>Understanding the Role of a Manager</li>
  </ul>

  <div class="exercise">
    <h2 class="exercise-title">Exercise 1: <span>EXPECTATIONS</span></h2>
    <p class="exercise-note">List the five most important expectations to be considered successful in your role.</p>
  </div>
  <table class="expectations">
    <tr><th class="blank"></th><th>FIVE MOST IMPORTANT EXPECTATIONS OF MY ROLE</th></tr>
    <tr><td class="num">01</td><td></td></tr>
    <tr><td class="num">02</td><td></td></tr>
    <tr><td class="num">03</td><td></td></tr>
    <tr><td class="num">04</td><td></td></tr>
    <tr><td class="num">05</td><td></td></tr>
    <tr class="spare"><td></td><td></td></tr>
  </table>
</section>

<!-- Outer spread: back + front cover -->
<section class="spread outer-spread" aria-label="Back and front cover spread">
  <svg class="art" viewBox="0 0 1040 735">
    <polygon points="330,0 520,0 520,150" fill="var(--brand)"/>
    <polygon points="300,0 330,0 520,150 520,175" fill="var(--brand)"/>
  </svg>
  <div class="back-ghost" aria-hidden="true">NORVA</div>
  <div class="back-wordmark">NORVA</div>
  <address class="back-address">
    Norva Holding A/S<br>
    Havnevej 12<br>
    8150 Aarlund, DENMARK<br>
    T: +45 0000 1234<br>
    CVR: 12345678
  </address>
  <section class="page front-cover" aria-label="Front cover">
    <svg class="art" viewBox="0 0 520 735"><use href="#cover-art"/></svg>
    <div class="cover-title">
      <div class="wordmark">NORVA</div>
      <h1 class="cover-heading">LEADERSHIP</h1>
      <p class="cover-sub">PROFILE DESIGN 2023</p>
      <div class="cover-rule"></div>
    </div>
  </section>
</section>

</body>
</html>
```